VelmorDrops (Foundational) Product Label

Ok. Soooo...I have a "high-end" hair nourishing/care product line that needs a "foundational" label - slightly alerted for various formulas. My products are all natural and do not contain artificial ingredients or preservatives and will need a label that will attract multicultural consumers that want gentle, caring products.

What am I looking for? Good question! I just know that I'm looking an elegant, yet creative, colorful, modern label that will look fabulous especially on Tavrel Glass 30 and 50 ml pipette bottles. (Please Google it since I can't add links to this brief.)

Additionally, I have two logos that need adding to the bottle, which can be emailed to you. I'll need to be able to add a barcode and list of ingredients to the label...most of which are proprietary blends and will most likely by listed as such.

As I've told other designers, I don't always know what I want, but will know it when I see it. I hope to closeout this project within 15 days (I added time to travel for a wedding and may not respond as quickly as I may want).

Thank you for your interest and I look forward to seeing your creations!!
Updates

Please add "SHAKE WELL. Product may separate." immediately after the words "Recommended use:".

Target Market(s)

Unisex, multicultural, consumers with natural or processed hair.

Industry/Entity Type

Hair

Font styles to use
Script

Requirements
Must have
• Some color...I like natural and neutral colors, but want splashes of color that pop.
• Label details:
• I've already uploaded the logos to the project brief. You have my permission to refine/change the logos to meet your creative design. The "(TM)" is for the "trademark symbol"
• Product: VelmorDrops(TM) by QuindaloGraced(TM) Nourishing Hair and Scalp Oil Blend
• Unit: 50 mL
• PRECAUTIONS: FOR EXTERNAL USE ONLY. If ingested contact your local Poison Control Office. Keep away from open flames. Avoid direct sunlight. Keep out of reach of children. Consult a physician if pregnant.
• Ingredients: Cocos nucifera (Coconut Oil), Olea europaea L. (Extra Virgin Olive Oil), Ricinus Communis (Castor Oil), Vitis vinifera L. (Grapeseed Oil), Butyrospermum parkii (Shea Butter),  Carthamus tinctorius L. (Safflower Oil),  Prunus dulcis (Sweet Almond Oil), and other ingredients.
• Recommended use: Apply sparingly to clean scalp and hair and gently massage. Style as usual. A little goes a long way so repeat application only as needed to avoid saturation.
• For additional information please visit www.VelmorDrops.example or email us at
• Info@VelmorDrops.example
• Created and Distributed by:
• Loretta Brimsby-Kane Ventures, LLC, Halbrook, VA 20917
• (855) 307-4192
Nice to have
• I THINK I would like to see pictures of Shea, coconuts, olives, open grapes showing the seeds...something to help tell the story about the all-natural ingredients. As for the font, I do like script styles, but the packaging isn't for me...nor has to attract me...so I need fonts, colors, and a layout that will attract both women AND men.
Should not have
• I don't want pictures of models, or people or anything that could steer the products from one culture to another. Anyone with skin and/or hair can use my oils (and bath minerals).

```html
<!DOCTYPE html>
<html lang="en">
<head>
<meta charset="utf-8">
<title>VelmorDrops – Nourishing Hair and Scalp Oil Blend Labels</title>
<link rel="stylesheet" href="https://fonts.googleapis.com/css2?family=Dancing+Script:wght@500&family=Lato:wght@400;700&display=swap">
<style>
  :root {
    --page-top: #dcdcdc;
    --page-bottom: #f7f7f7;
    --label-white: #ffffff;
    --ink: #3a3a3a;
    --ink-soft: #6b6b6b;
    --sand: #c5bba9;
    --leaf: #3e9656;
    --sky: #b4cde2;
    --lake: #8db1d3;
    --mist: #cfe0ec;
    --seed-brown: #9a6a45;
    --leaf-green: #7ea35a;
    --berry: #b4545a;
  }
  * { box-sizing: border-box; margin: 0; padding: 0; }
  html, body { width: 1200px; height: 640px; overflow: hidden; }
  body {
    background: linear-gradient(180deg, var(--page-top) 0%, var(--page-bottom) 55%, #ffffff 100%);
    font-family: "Lato", Arial, sans-serif;
    color: var(--ink);
  }
  .label-set {
    position: absolute;
    left: 35px; top: 185px;
    display: flex; gap: 22px;
  }
  .label {
    position: relative;
    width: 170px; height: 270px;
    background: var(--label-white);
    box-shadow: 0 2px 10px rgba(0,0,0,.12);
    overflow: hidden;
  }
  .label--sand  { --tone: var(--sand); --logo: #4a4a4a; }
  .label--leaf  { --tone: var(--leaf); --logo: var(--leaf); }
  .label--sky   { --tone: var(--sky);  --logo: #4a4a4a; }
  .label--lake  { --tone: var(--lake); --logo: #5c86b0; }

  .brand {
    position: absolute; left: 12px; top: 10px;
    display: flex; align-items: center; gap: 5px;
  }
  .brand__dot {
    width: 9px; height: 9px; border-radius: 50%;
    background: var(--logo, var(--ink));
  }
  .brand__name {
    font-family: "Dancing Script", cursive;
    font-weight: 500; font-size: 21px; line-height: 1;
    color: var(--logo, var(--ink));
  }
  .brand__by {
    position: absolute; left: 26px; top: 33px;
    font-size: 5.5px; letter-spacing: .4px; color: var(--ink-soft);
    text-transform: uppercase;
  }

  .band {
    position: absolute; left: 0; top: 44px;
    width: 170px; height: 112px;
    color: var(--tone);
  }
  .band svg { display: block; width: 100%; height: 100%; }
  .title {
    position: absolute; left: 0; top: 56px; width: 170px;
    text-align: center; color: #ffffff;
    font-family: "Dancing Script", cursive; font-weight: 500;
  }
  .title__kind { display: block; font-size: 16px; line-height: 1.1; opacity: .95; }
  .title__line { display: block; font-size: 22px; line-height: 1.15; }

  .ingredient-art {
    position: absolute; left: 14px; top: 170px;
    width: 142px; height: 84px; border-radius: 40% 45% 40% 45%;
    background:
      radial-gradient(ellipse 20% 26% at 20% 55%, var(--berry), transparent 70%),
      radial-gradient(ellipse 30% 30% at 50% 52%, var(--seed-brown), transparent 72%),
      radial-gradient(ellipse 26% 40% at 80% 50%, #b9cf86, transparent 72%),
      radial-gradient(ellipse 60% 55% at 50% 40%, var(--leaf-green), transparent 75%);
    opacity: .9;
  }
  .volume {
    position: absolute; right: 10px; bottom: 6px;
    font-size: 6px; color: var(--ink-soft);
  }

  .label--back { padding: 44px 12px 0; }
  .label--back-mist { background: var(--mist); }
  .label--back .brand { left: 50%; transform: translateX(-50%); --logo: #4a4a4a; }
  .label--back .brand__by { left: 50%; transform: translateX(-50%); white-space: nowrap; }
  .back-copy { position: relative; z-index: 1; }
  .back-copy p {
    font-size: 6px; line-height: 1.4; color: var(--ink);
    margin-bottom: 5px;
  }
  .back-copy strong { font-weight: 700; }
  .label--back-mist .back-copy p { color: #50657a; }
  .back-art {
    position: absolute; right: 8px; bottom: 14px;
    width: 90px; height: 150px; border-radius: 45% 45% 30% 30%;
    background: linear-gradient(180deg, rgba(110,140,160,.10), rgba(110,140,160,.22));
  }
</style>
</head>
<body>
<main class="label-set">

  <section class="label label--sand">
    <div class="brand"><span class="brand__dot"></span><span class="brand__name">VelmorDrops</span></div>
    <span class="brand__by">by QuindaloGraced</span>
    <div class="band"><svg viewBox="0 0 170 112" preserveAspectRatio="none"><path d="M0 8 Q45 0 90 6 T170 3 L170 92 Q125 106 80 96 T0 102 Z" fill="currentColor"/></svg></div>
    <h2 class="title"><span class="title__kind">Nourishing</span><span class="title__line">Hair and Scalp</span><span class="title__line">Oil Blend</span></h2>
    <div class="ingredient-art" role="img" aria-label="Illustration of shea nuts, leaves, coconut and olives"></div>
    <span class="volume">50 mL</span>
  </section>

  <section class="label label--leaf">
    <div class="brand"><span class="brand__dot"></span><span class="brand__name">VelmorDrops</span></div>
    <span class="brand__by">by QuindaloGraced</span>
    <div class="band"><svg viewBox="0 0 170 112" preserveAspectRatio="none"><path d="M0 8 Q45 0 90 6 T170 3 L170 92 Q125 106 80 96 T0 102 Z" fill="currentColor"/></svg></div>
    <h2 class="title"><span class="title__kind">Nourishing</span><span class="title__line">Hair and Scalp</span><span class="title__line">Oil Blend</span></h2>
    <div class="ingredient-art" role="img" aria-label="Illustration of shea nuts, leaves, coconut and olives"></div>
    <span class="volume">50 mL</span>
  </section>

  <section class="label label--sky">
    <div class="brand"><span class="brand__dot"></span><span class="brand__name">VelmorDrops</span></div>
    <span class="brand__by">by QuindaloGraced</span>
    <div class="band"><svg viewBox="0 0 170 112" preserveAspectRatio="none"><path d="M0 8 Q45 0 90 6 T170 3 L170 92 Q125 106 80 96 T0 102 Z" fill="currentColor"/></svg></div>
    <h2 class="title"><span class="title__kind">Nourishing</span><span class="title__line">Hair and Scalp</span><span class="title__line">Oil Blend</span></h2>
    <div class="ingredient-art" role="img" aria-label="Illustration of shea nuts, leaves, coconut and olives"></div>
    <span class="volume">50 mL</span>
  </section>

  <section class="label label--lake">
    <div class="brand"><span class="brand__dot"></span><span class="brand__name">VelmorDrops</span></div>
    <span class="brand__by">by QuindaloGraced</span>
    <div class="band"><svg viewBox="0 0 170 112" preserveAspectRatio="none"><path d="M0 8 Q45 0 90 6 T170 3 L170 92 Q125 106 80 96 T0 102 Z" fill="currentColor"/></svg></div>
    <h2 class="title"><span class="title__kind">Nourishing</span><span class="title__line">Hair and Scalp</span><span class="title__line">Oil Blend</span></h2>
    <div class="ingredient-art" role="img" aria-label="Illustration of shea nuts, leaves, coconut and olives"></div>
    <span class="volume">50 mL</span>
  </section>

  <section class="label label--back">
    <div class="brand"><span class="brand__dot"></span><span class="brand__name">VelmorDrops</span></div>
    <span class="brand__by">by QuindaloGraced</span>
    <div class="back-art" role="img" aria-label="Faint line illustration decorating the back label"></div>
    <div class="back-copy">
      <p><strong>PRECAUTIONS:</strong> FOR EXTERNAL USE ONLY. Keep away from open flames and direct sunlight. Keep out of reach of children.</p>
      <p><strong>Ingredients:</strong> Coconut, Olive, Castor, Grapeseed, Safflower and Sweet Almond Oils, Shea Butter and other ingredients.</p>
      <p><strong>Recommended use:</strong> SHAKE WELL. Product may separate. Apply sparingly to clean scalp and hair and gently massage.</p>
      <p>For additional information please visit www.VelmorDrops.example<br>Info@VelmorDrops.example</p>
      <p>Created and Distributed by:<br>Loretta Brimsby-Kane Ventures, LLC<br>Halbrook, VA 20917<br>(855) 307-4192</p>
      <p>50 mL</p>
    </div>
  </section>

  <section class="label label--back label--back-mist">
    <div class="brand"><span class="brand__dot"></span><span class="brand__name">VelmorDrops</span></div>
    <span class="brand__by">by QuindaloGraced</span>
    <div class="back-art" role="img" aria-label="Faint line illustration decorating the back label"></div>
    <div class="back-copy">
      <p><strong>PRECAUTIONS:</strong> FOR EXTERNAL USE ONLY. Keep away from open flames and direct sunlight. Keep out of reach of children.</p>
      <p><strong>Ingredients:</strong> Coconut, Olive, Castor, Grapeseed, Safflower and Sweet Almond Oils, Shea Butter and other ingredients.</p>
      <p><strong>Recommended use:</strong> SHAKE WELL. Product may separate. Apply sparingly to clean scalp and hair and gently massage.</p>
      <p>For additional information please visit www.VelmorDrops.example<br>Info@VelmorDrops.example</p>
      <p>Created and Distributed by:<br>Loretta Brimsby-Kane Ventures, LLC<br>Halbrook, VA 20917<br>(855) 307-4192</p>
      <p>50 mL</p>
    </div>
  </section>

</main>
</body>
</html>
```